Create Design for Business Folders

We need a new design for business folders we will be having printed. The size of the folders are 9X12, and a template can be downloaded from www.pelmarkstudio-example.com. We are using the standard size folders, full color printing on the front only.

Since this is a folder and not a brochure, we do not need a lot of text on the folder. The design is the important issue. It should be bright and colorful enough to take advantage of the full color printing. Branding is important, but this should be easy. Our logo and theme is very common, and there are many stock photos that can be used to create an excellent design.

Basically our theme or branding involves rising color bars indicating a rising credit score. I would like something creative designed around this theme. I do not simply want our logo blown up as the theme. Something highly creative and imaginative is preferred

I would prefer a background that is colorful and covers the entire brochure.

The only thing on the front of the brochure is "Tally Peak Lending" "Lift Every Number, Brighten Every Day"

On the back would be our contact information, with address, phone, web, etc.

Industry/Entity Type

Printing

Font styles to use
Sans Serif

Colors
3276b5
0355a3
ffffff

Requirements
Should not have
• Nothing to dark.

```html
<!DOCTYPE html>
<html lang="en">
<head>
<meta charset="utf-8">
<title>Tally Peak Lending – Business Folder</title>
<link href="https://fonts.googleapis.com/css2?family=Exo+2:wght@300;400;600&display=swap" rel="stylesheet">
<style>
  :root {
    --blue-main: #3276b5;
    --blue-deep: #0355a3;
    --blue-bright: #5b9be0;
    --blue-soft: #9cc6ee;
    --blue-mist: #dbeaf8;
    --blue-haze: #eef5fc;
    --paper: #ffffff;
    --backdrop: #e3e3e3;
    --ink-soft: #5a6f86;
    --ink-head: #55575a;
    --photo-top: #f4f5f6;
    --photo-mid: #d9d4cc;
    --photo-bottom: #a7a096;
  }
  * { box-sizing: border-box; margin: 0; padding: 0; }
  html, body { width: 1200px; height: 1000px; overflow: hidden; }
  body {
    background: var(--backdrop);
    font-family: "Exo 2", "Segoe UI", sans-serif;
    position: relative;
  }
  .folder-panel {
    position: absolute;
    top: 170px;
    width: 500px;
    height: 660px;
    background:
      radial-gradient(ellipse 90% 55% at 50% 52%, var(--paper) 0%, var(--paper) 45%, var(--blue-haze) 80%, var(--blue-mist) 100%);
    box-shadow: 0 8px 26px rgba(0,0,0,0.14);
    overflow: hidden;
  }
  .folder-panel--back { left: 60px; }
  .folder-panel--front { left: 640px; }
  .wave-art { position: absolute; left: 0; width: 100%; }
  .wave-art--top { top: 0; height: 250px; }
  .wave-art--bottom { top: 410px; height: 250px; }

  .team-photo {
    position: absolute;
    left: 22px;
    top: 120px;
    width: 456px;
    height: 280px;
    border-radius: 50% / 42%;
    background: linear-gradient(180deg, var(--photo-top) 0%, var(--photo-mid) 45%, var(--photo-bottom) 100%);
  }
  .front-headline {
    position: absolute;
    left: 44px;
    top: 404px;
    font-weight: 300;
    font-size: 19px;
    line-height: 1.3;
    color: var(--ink-head);
    transform: rotate(-3deg);
    transform-origin: left top;
  }
  .brand-block {
    position: absolute;
    right: 28px;
    bottom: 30px;
    text-align: right;
  }
  .brand-name {
    display: flex;
    align-items: center;
    justify-content: flex-end;
    gap: 8px;
    font-weight: 600;
    font-size: 23px;
    line-height: 1;
    color: var(--blue-main);
  }
  .brand-mark {
    width: 18px; height: 18px;
    background: var(--blue-main);
  }
  .brand-tagline {
    margin-top: 5px;
    font-weight: 600;
    font-size: 8.5px;
    letter-spacing: 0.5px;
    color: var(--blue-main);
  }
  .contact-list {
    position: absolute;
    left: 40px;
    bottom: 36px;
    list-style: none;
    font-size: 10px;
    font-weight: 400;
    color: var(--ink-soft);
    line-height: 1.45;
  }
  .contact-list li { display: flex; align-items: flex-start; gap: 6px; }
  .contact-icon { width: 9px; height: 9px; margin-top: 3px; flex: none; fill: var(--blue-main); }
</style>
</head>
<body>

<section class="folder-panel folder-panel--back" aria-label="Folder back">
  <svg class="wave-art wave-art--top" viewBox="0 0 500 250" preserveAspectRatio="none" aria-hidden="true">
    <defs>
      <linearGradient id="backSweep" x1="0" y1="0" x2="1" y2="0">
        <stop offset="0" stop-color="#ffffff" stop-opacity="0"/>
        <stop offset="0.5" stop-color="var(--blue-soft)"/>
        <stop offset="1" stop-color="var(--blue-main)"/>
      </linearGradient>
      <linearGradient id="backHaze" x1="0" y1="0" x2="1" y2="0">
        <stop offset="0" stop-color="var(--blue-haze)" stop-opacity="0.3"/>
        <stop offset="1" stop-color="var(--blue-mist)"/>
      </linearGradient>
    </defs>
    <path d="M0 0 L500 0 L500 170 C360 120 180 150 0 230 Z" fill="url(#backHaze)"/>
    <path d="M90 200 C220 90 360 40 500 25 L500 75 C360 80 220 130 90 200 Z" fill="url(#backSweep)"/>
    <path d="M160 150 C280 80 390 45 500 35" stroke="#ffffff" stroke-width="2" fill="none" opacity="0.9"/>
    <path d="M0 230 C150 140 330 105 500 105 L500 118 C330 120 160 160 0 245 Z" fill="var(--blue-soft)" opacity="0.6"/>
  </svg>

  <ul class="contact-list">
    <li><svg class="contact-icon" viewBox="0 0 10 10"><path d="M5 0a3.5 3.5 0 0 0-3.5 3.5C1.5 6 5 10 5 10s3.5-4 3.5-6.5A3.5 3.5 0 0 0 5 0zm0 5a1.5 1.5 0 1 1 0-3 1.5 1.5 0 0 1 0 3z"/></svg><span>4820 Brightwater Lane, Suite B4<br>Harlow Springs, Vermont 05601</span></li>
    <li><svg class="contact-icon" viewBox="0 0 10 10"><path d="M2 0l2 2.5-1 1.2a6 6 0 0 0 3.3 3.3l1.2-1L10 8 8.5 10C4 10 0 6 0 1.5z"/></svg><span>(800)555-0148</span></li>
    <li><svg class="contact-icon" viewBox="0 0 10 10"><rect x="0" y="3" width="10" height="6" rx="1"/><rect x="2" y="0" width="6" height="3"/></svg><span>(800)555-0193</span></li>
    <li><svg class="contact-icon" viewBox="0 0 10 10"><path d="M0 2h10v6H0z M0 2l5 3.5L10 2" fill="none" stroke="var(--blue-main)" stroke-width="1.2"/></svg><span>hello@tallypeak-example.com</span></li>
    <li><svg class="contact-icon" viewBox="0 0 10 10"><circle cx="5" cy="5" r="4.3" fill="none" stroke="var(--blue-main)" stroke-width="1.2"/><path d="M0.7 5h8.6M5 0.7c-2 2.5-2 6 0 8.6M5 0.7c2 2.5 2 6 0 8.6" fill="none" stroke="var(--blue-main)" stroke-width="0.8"/></svg><span>www.tallypeak-example.com</span></li>
  </ul>
</section>

<section class="folder-panel folder-panel--front" aria-label="Folder front">
  <svg class="wave-art wave-art--top" viewBox="0 0 500 250" preserveAspectRatio="none" aria-hidden="true">
    <defs>
      <linearGradient id="frontSweep" x1="0" y1="0" x2="1" y2="0">
        <stop offset="0" stop-color="var(--blue-main)"/>
        <stop offset="0.45" stop-color="var(--blue-bright)"/>
        <stop offset="1" stop-color="var(--blue-soft)" stop-opacity="0.4"/>
      </linearGradient>
      <linearGradient id="frontHaze" x1="0" y1="0" x2="0" y2="1">
        <stop offset="0" stop-color="var(--blue-mist)"/>
        <stop offset="1" stop-color="#ffffff" stop-opacity="0"/>
      </linearGradient>
    </defs>
    <rect width="500" height="250" fill="url(#frontHaze)"/>
    <path d="M0 0 L500 0 L500 55 C330 20 160 45 0 110 Z" fill="url(#frontSweep)"/>
    <path d="M0 35 C160 5 340 15 500 75" stroke="#ffffff" stroke-width="3" fill="none"/>
    <path d="M0 120 C160 60 330 55 500 95 L500 125 C330 88 170 100 0 150 Z" fill="var(--blue-soft)" opacity="0.7"/>
    <path d="M0 150 C170 105 340 100 500 130 L500 140 C340 115 170 120 0 160 Z" fill="var(--blue-mist)"/>
  </svg>

  <div class="team-photo" role="img" aria-label="Photo of five business people in suits standing with arms crossed on a white backdrop"></div>

  <svg class="wave-art wave-art--bottom" viewBox="0 0 500 250" preserveAspectRatio="none" aria-hidden="true">
    <defs>
      <linearGradient id="frontLowSweep" x1="0" y1="0" x2="1" y2="0">
        <stop offset="0" stop-color="#ffffff" stop-opacity="0"/>
        <stop offset="0.5" stop-color="var(--blue-soft)"/>
        <stop offset="1" stop-color="var(--blue-main)"/>
      </linearGradient>
      <linearGradient id="frontLowHaze" x1="0" y1="0" x2="0" y2="1">
        <stop offset="0" stop-color="#ffffff" stop-opacity="0"/>
        <stop offset="1" stop-color="var(--blue-mist)"/>
      </linearGradient>
    </defs>
    <rect width="500" height="250" fill="url(#frontLowHaze)"/>
    <path d="M0 10 C170 -15 330 -20 500 -10 L500 30 C330 25 170 45 0 70 Z" fill="var(--blue-mist)"/>
    <path d="M40 175 C200 110 350 90 500 80 L500 135 C350 135 210 150 40 175 Z" fill="url(#frontLowSweep)"/>
    <path d="M0 140 C180 95 350 70 500 70" stroke="#ffffff" stroke-width="2" fill="none"/>
    <path d="M0 205 C170 160 340 150 500 158 L500 170 C340 165 170 175 0 220 Z" fill="var(--blue-soft)" opacity="0.6"/>
  </svg>

  <h1 class="front-headline">We Legally and Ethically<br>Raise Credit Scores</h1>

  <div class="brand-block">
    <div class="brand-name"><span class="brand-mark" aria-hidden="true"></span>Tally Peak Lending</div>
    <div class="brand-tagline">LIFT EVERY NUMBER, BRIGHTEN EVERY DAY!</div>
  </div>
</section>

</body>
</html>
```